Our landing page needs to be updated - 1 panel only - SEE NEW MESSAGE AND MOCK UP CONCEPT screenshot

We require the top page of our landing page redesigned to better convey our product offering.

The application is an email marketing platform offering pre-designed and ready-to-use email templates.
The landing page should (a) visually convey our product proposition - ie - display a sample of the email templates (resources provided) and also (b) in copy format explain our product proposition.

There are SIX categories for the templates - on the attached resources these are explained.
You should visit VORTELL.COM - to see more information (and how bad our current landing page is)

It should be clear there are six categories - their headings are:

1. Message someone
2. Share important information
3. Promote Deals and Special Offers
4. Announce Events
5. Broadcast Newsletters
6. Advertise your Products or Services

These headings are only intended to explain why there are different template designs - they are secondary information

The copy hierarchy is:

Main sell
"Ready-To-Use Email Templates"

Supporting sell

"Insert your images and links then send. It’s that quick and easy.
Beautiful emails deliver better results."

Last sell checklist

"Free image library
300 plus designs
Email analytics"

The images (cropped as required) of our templates are the heroes - the copy should be supporting.

Purple is our primary brand colour

Logo is also provided

At vortell.com we like "Sign In" being held in a box

Our colour pallet is attached

NB - at Vortell.com - all panels will remain on the Landing page - other than the top panel - ie - above the fold - this is the one we require redesigning because the image of a female at a keyboard does not convey our product offering.

Button shapes should be consistent with those already on Vortell.com

Our Font family is LATO

Marketing

1 page

Requirements
Must have
• Our font family - LATO and our colour pallett
• Our sample email templates
• Top Right - navigation links - "Pricing Create Account Sign In"

```html
<!DOCTYPE html>
<html lang="en">
<head>
<meta charset="utf-8">
<title>Vortell – Ready-To-Use Email Templates</title>
<link rel="stylesheet" href="https://fonts.googleapis.com/css2?family=Lato:wght@300;400;700;900&display=swap">
<style>
:root{
  --purple:#8a2ba6;
  --ink:#2f3240;
  --text:#5b5f6b;
  --muted:#8a8e99;
  --line:#e3e5ea;
  --wash:#f4f5f9;
  --green:#3acb2c;
  --green-dark:#2fb324;
  --blue:#0ba2ea;
  --sky:#1aa8ee;
  --cat-yellow:#f3b62a;
  --cat-red:#f1615e;
  --cat-purple:#a35ae6;
  --cat-blue:#3b8ef0;
  --cat-teal:#20c5cf;
  --cat-green:#5cce57;
  --slate:#4a4c5a;
  --slate-dark:#3d3f4b;
  --pill:#9aa6bf;
  --white:#ffffff;
}
*{box-sizing:border-box;margin:0;padding:0}
html,body{width:1200px;height:3396px;overflow:hidden}
body{font-family:"Lato",sans-serif;color:var(--text);background:var(--white);position:relative}
section,header,footer{position:absolute;left:0;width:1200px}
.center{text-align:center}
.btn{display:inline-block;height:30px;line-height:30px;padding:0 22px;border-radius:15px;color:var(--white);font-size:11px;font-weight:700;text-decoration:none}
.btn--green{background:var(--green)}
.btn--blue{background:var(--sky)}

/* nav */
.site-nav{top:0;height:44px}
.brand{position:absolute;left:233px;top:10px;font-size:20px;font-weight:700;color:var(--purple)}
.nav-links{position:absolute;right:232px;top:11px;display:flex;align-items:center;gap:34px;font-size:11px;color:var(--ink)}
.nav-signin{border:1px solid var(--ink);border-radius:11px;padding:3px 12px}

/* hero */
.hero{top:0;height:561px}
.hero-title{position:absolute;top:106px;width:100%;font-size:33px;font-weight:700;color:var(--ink)}
.hero-sub{position:absolute;top:162px;width:100%;font-size:12.5px;line-height:19px;color:var(--muted)}
.checklist{position:absolute;top:216px;width:100%;display:flex;justify-content:center;gap:26px;font-size:11px;color:var(--ink)}
.checklist li{list-style:none;display:flex;align-items:center;gap:8px}
.check-box{width:11px;height:11px;border:2px solid var(--slate);border-radius:2px}
.hero-actions{position:absolute;top:268px;width:100%;display:flex;justify-content:center;gap:18px}
.hero-actions .btn{width:113px;padding:0;text-align:center}

/* templates strip */
.templates{top:407px;left:48px;width:1104px;display:flex;justify-content:space-between;z-index:2}
.template-card{width:168px;background:var(--white);box-shadow:0 2px 6px rgba(0,0,0,.12)}
.template-label{height:38px;display:flex;align-items:center;justify-content:center;text-align:center;font-size:9.5px;line-height:11px;font-weight:700;color:var(--white);padding:0 14px}
.template-preview{height:212px}
.cat-yellow .template-label{background:var(--cat-yellow)}
.cat-red .template-label{background:var(--cat-red)}
.cat-purple .template-label{background:var(--cat-purple)}
.cat-blue .template-label{background:var(--cat-blue)}
.cat-teal .template-label{background:var(--cat-teal)}
.cat-green .template-label{background:var(--cat-green)}
.cat-yellow .template-preview{background:linear-gradient(180deg,#2fc7d8 0 32%,#f7f7f7 32%)}
.cat-red .template-preview{background:linear-gradient(180deg,#fff 0 18%,#3bb7a8 18% 66%,#f5f5f5 66%)}
.cat-purple .template-preview{background:linear-gradient(180deg,#fff 0 14%,#6d6a66 14% 90%,#f5f5f5 90%)}
.cat-blue .template-preview{background:linear-gradient(180deg,#c9ccd1 0 22%,#fff 22% 60%,#f0f0f0 60%)}
.cat-teal .template-preview{background:linear-gradient(180deg,#fff 0 40%,#d9b99a 40% 82%,#f3f3f3 82%)}
.cat-green .template-preview{background:linear-gradient(180deg,#fff 0 12%,#1e9be6 12% 48%,#e9eef3 48%)}

/* business section */
.business{top:561px;height:763px;background:var(--wash)}
.section-title{font-size:21px;font-weight:700;color:var(--ink)}
.section-sub{font-size:11.5px;color:var(--text)}
.business .section-title{position:absolute;top:191px;width:100%}
.business .section-sub{position:absolute;top:238px;width:100%}
.device-art{position:absolute;left:346px;top:299px;width:503px;height:283px;border-radius:6px;background:linear-gradient(135deg,#dfe3ea 0%,#f7f8fa 45%,#d7dbe2 100%)}
.business .btn{position:absolute;top:631px;left:525px;width:150px;padding:0;text-align:center}

/* steps */
.steps{top:1324px;height:533px}
.steps .section-title{position:absolute;top:96px;width:100%}
.step-row{position:absolute;top:168px;left:233px;width:735px;display:flex;justify-content:space-between}
.step{width:150px;text-align:center}
.step-art{width:86px;height:90px;margin:0 auto;border-radius:8px;background:linear-gradient(135deg,#dff0fc,#bfe2f8)}
.step-name{margin-top:30px;font-size:11px;font-weight:700;color:var(--ink)}
.step-text{margin-top:8px;font-size:9px;line-height:12.5px;color:var(--muted)}
.steps .btn{position:absolute;top:405px;left:512px;width:176px;padding:0;text-align:center}

/* audience */
.audience{top:1857px;height:627px;background:var(--blue);color:var(--white)}
.audience .section-title{position:absolute;top:96px;width:100%;color:var(--white)}
.audience .section-sub{position:absolute;top:140px;width:100%;color:var(--white);font-weight:700}
.audience-grid{position:absolute;top:200px;left:233px;width:735px;display:grid;grid-template-columns:repeat(3,1fr);row-gap:40px}
.persona{text-align:center;padding:0 38px}
.persona svg{width:60px;height:60px;display:block;margin:0 auto}
.persona-name{margin-top:14px;font-size:11px;font-weight:700}
.persona-text{margin-top:9px;font-size:9px;line-height:12.5px;color:rgba(255,255,255,.85)}

/* pricing */
.pricing{top:2484px;height:572px}
.pricing .section-title{position:absolute;top:95px;width:100%}
.plans{position:absolute;top:174px;left:233px;width:745px;display:flex;align-items:flex-start}
.plan{width:148px;text-align:center;font-size:9px;color:var(--muted);border-right:1px solid var(--line)}
.plan:last-child{border-right:0}
.plan-head{height:45px;line-height:45px;background:var(--wash);font-size:11px;color:var(--ink)}
.plan-cell{height:42px;display:flex;align-items:center;justify-content:center;border-bottom:1px solid var(--line);line-height:12px;padding:0 18px}
.plan-price{color:var(--ink);font-weight:700}
.plan .btn{margin-top:10px;height:26px;line-height:26px;width:74px;padding:0;background:var(--pill);border-radius:13px;font-weight:400}
.plan--featured{width:156px;margin-top:-25px;padding-bottom:24px;background:var(--green);color:var(--white);border-radius:4px;border-right:0;box-shadow:0 4px 10px rgba(0,0,0,.15)}
.plan--featured .plan-head{height:70px;line-height:80px;background:transparent;color:var(--white);font-weight:700}
.plan--featured .plan-cell{border-color:rgba(255,255,255,.35);color:var(--white)}
.plan--featured .plan-price{color:var(--white)}
.plan--featured .btn{background:var(--white);color:var(--ink)}

/* footer */
.site-footer{top:3056px;height:281px;background:var(--slate);color:var(--white)}
.footer-brand{position:absolute;top:96px;width:100%;font-size:30px;font-weight:700}
.footer-links{position:absolute;top:172px;width:100%;display:flex;justify-content:center;gap:46px;font-size:9.5px;color:rgba(255,255,255,.85)}
.legal-bar{top:3337px;height:59px;background:var(--slate-dark);color:rgba(255,255,255,.6);font-size:8.5px}
.legal-bar p{position:absolute;left:233px;top:24px}
.social{position:absolute;right:226px;top:19px;display:flex;gap:14px}
.social span{width:20px;height:20px;border-radius:3px;background:rgba(255,255,255,.55)}
</style>
</head>
<body>

<header class="site-nav">
  <div class="brand">Vortell</div>
  <nav class="nav-links">
    <span>Pricing</span>
    <span>Create Account</span>
    <span class="nav-signin">Sign in</span>
  </nav>
</header>

<section class="hero center">
  <h1 class="hero-title">Ready-To-Use Email Templates</h1>
  <p class="hero-sub">Insert your images and links then send. It’s that quick and easy.<br>Beautiful emails deliver better results.</p>
  <ul class="checklist">
    <li><i class="check-box"></i>Free image library</li>
    <li><i class="check-box"></i>300 plus designs</li>
    <li><i class="check-box"></i>Email analytics</li>
  </ul>
  <div class="hero-actions">
    <a class="btn btn--green">View Templates</a>
    <a class="btn btn--blue">Free Trial</a>
  </div>
</section>

<section class="business center">
  <h2 class="section-title">Email templates for every business</h2>
  <p class="section-sub">Professionally designed, responsive, mobile-ready templates.</p>
  <div class="device-art" role="img" aria-label="Email template shown on laptop, desktop, tablet and phone screens"></div>
  <a class="btn btn--green">View our template gallery</a>
</section>

<div class="templates" style="position:absolute">
  <article class="template-card cat-yellow"><div class="template-label">Message someone</div><div class="template-preview" role="img" aria-label="Patterned header email template with letter text"></div></article>
  <article class="template-card cat-red"><div class="template-label">Share important information</div><div class="template-preview" role="img" aria-label="Email template with flower photo and heading"></div></article>
  <article class="template-card cat-purple"><div class="template-label">Promote Deals and Special Offers</div><div class="template-preview" role="img" aria-label="Email template with product photo and offer heading"></div></article>
  <article class="template-card cat-blue"><div class="template-label">Announce Events</div><div class="template-preview" role="img" aria-label="Event announcement email template with logo and text"></div></article>
  <article class="template-card cat-teal"><div class="template-label">Broadcast Newsletters</div><div class="template-preview" role="img" aria-label="Newsletter email template with portrait photo"></div></article>
  <article class="template-card cat-green"><div class="template-label">Advertise your Products or Services</div><div class="template-preview" role="img" aria-label="Advertising email template with laptop photo"></div></article>
</div>

<section class="steps">
  <h2 class="section-title center">Beautiful emails by you... in seconds.</h2>
  <div class="step-row">
    <div class="step"><div class="step-art" role="img" aria-label="Template selection illustration"></div><h3 class="step-name">Select your template</h3><p class="step-text">World class designers have created the largest gallery of beautiful email templates in the world.</p></div>
    <div class="step"><div class="step-art" role="img" aria-label="Writing copy illustration"></div><h3 class="step-name">Write your copy</h3><p class="step-text">Simply edit your copy within our template using our custom designed email builder.</p></div>
    <div class="step"><div class="step-art" role="img" aria-label="Adding images illustration"></div><h3 class="step-name">Add your images</h3><p class="step-text">Upload images, logos or graphics and link to your website to drive reader interaction.</p></div>
    <div class="step"><div class="step-art" role="img" aria-label="Sending to recipients illustration"></div><h3 class="step-name">Add recipients and send!</h3><p class="step-text">That’s it. The fastest and easiest way to create and send stunning email, which get results!</p></div>
  </div>
  <a class="btn btn--green">Sign up and receive free credits!</a>
</section>

<section class="audience center">
  <h2 class="section-title">Who should use Vortell?</h2>
  <p class="section-sub">When you need quick, easy &amp; impressive email</p>
  <div class="audience-grid">
    <div class="persona">
      <svg viewBox="0 0 60 60" fill="none" stroke="#fff" stroke-width="2"><circle cx="28" cy="32" r="20"/><circle cx="28" cy="32" r="12"/><circle cx="28" cy="32" r="4"/><path d="M28 32L50 10M44 10h6v6"/></svg>
      <h3 class="persona-name">Sales &amp; Marketing Teams</h3><p class="persona-text">Get better results using world-class email templates incorporating analytics</p>
    </div>
    <div class="persona">
      <svg viewBox="0 0 60 60" fill="none" stroke="#fff" stroke-width="2"><circle cx="30" cy="12" r="5"/><path d="M23 26a7 7 0 0114 0"/><path d="M30 28v8M14 36h32M14 36v6M46 36v6"/><circle cx="14" cy="46" r="4"/><circle cx="46" cy="46" r="4"/></svg>
      <h3 class="persona-name">Professional Services</h3><p class="persona-text">Build client confidence and retention using professionally designed email templates.</p>
    </div>
    <div class="persona">
      <svg viewBox="0 0 60 60" fill="none" stroke="#fff" stroke-width="2"><path d="M8 22l4-12h36l4 12z"/><path d="M8 22h44v6H8z"/><path d="M12 28v24h36V28"/><rect x="18" y="34" width="10" height="18"/><rect x="33" y="34" width="10" height="8"/></svg>
      <h3 class="persona-name">Small Business Owners</h3><p class="persona-text">Communicate as a professional to be trusted using our business and marketing email templates.</p>
    </div>
    <div class="persona">
      <svg viewBox="0 0 60 60" fill="none" stroke="#fff" stroke-width="2"><rect x="22" y="8" width="16" height="16"/><path d="M30 12v8M26 16h8"/><path d="M6 40h10l10 4h12a3 3 0 000-6h-8M16 40v12h-10M38 44l14-6"/></svg>
      <h3 class="persona-name">Healthcare &amp; Education</h3><p class="persona-text">Keep everyone informed and promote your Friendloop and Vidstream activity</p>
    </div>
    <div class="persona">
      <svg viewBox="0 0 60 60" fill="none" stroke="#fff" stroke-width="2"><path d="M30 6l7 15 16 2-12 11 3 16-14-8-14 8 3-16L7 23l16-2z"/></svg>
      <h3 class="persona-name">Entertainment &amp; Retail</h3><p class="persona-text">Quickly and easily email your special offers and promotions to your existing customers</p>
    </div>
    <div class="persona">
      <svg viewBox="0 0 60 60" fill="none" stroke="#fff" stroke-width="2"><ellipse cx="30" cy="30" rx="24" ry="9"/><ellipse cx="30" cy="30" rx="24" ry="9" transform="rotate(60 30 30)"/><ellipse cx="30" cy="30" rx="24" ry="9" transform="rotate(-60 30 30)"/><circle cx="30" cy="30" r="3"/></svg>
      <h3 class="persona-name">Associations &amp; NGOs</h3><p class="persona-text">Impress stakeholders with sophisticated emails created and sent by you in seconds</p>
    </div>
  </div>
</section>

<section class="pricing">
  <h2 class="section-title center">Our pricing</h2>
  <div class="plans">
    <div class="plan"><div class="plan-head">Test Drive</div><div class="plan-cell plan-price">FREE</div><div class="plan-cell">Three FREE broadcasts</div><div class="plan-cell">No credit card required</div><div class="plan-cell">$500 free email credits</div><a class="btn">Select</a></div>
    <div class="plan"><div class="plan-head">Pay As You Go</div><div class="plan-cell plan-price">$7.95</div><div class="plan-cell">Per broadcast</div><div class="plan-cell">Pay only when you broadcast</div><div class="plan-cell">Cost per email address from 1 cent</div><a class="btn">Select</a></div>
    <div class="plan plan--featured"><div class="plan-head">Bronze Monthly Plan</div><div class="plan-cell plan-price">$9.95</div><div class="plan-cell">3 broadcasts per month</div><div class="plan-cell">Pause or cancel anytime<br>No questions asked</div><div class="plan-cell">Cost per email address from 1 cent</div><a class="btn">Select</a></div>
    <div class="plan"><div class="plan-head">Silver Monthly Plan</div><div class="plan-cell plan-price">$12.95</div><div class="plan-cell">10 broadcasts per month</div><div class="plan-cell">Pause or cancel anytime<br>No questions asked</div><div class="plan-cell">Cost per email address from 1 cent</div><a class="btn">Select</a></div>
    <div class="plan"><div class="plan-head">Gold Monthly Plan</div><div class="plan-cell plan-price">$24.95</div><div class="plan-cell">100 broadcasts per month</div><div class="plan-cell">Pause or cancel anytime<br>No questions asked</div><div class="plan-cell">Cost per email address from 1 cent</div><a class="btn">Select</a></div>
  </div>
</section>

<footer class="site-footer center">
  <div class="footer-brand">Vortell</div>
  <nav class="footer-links">
    <span>Blog</span><span>Designer's Toolkit</span><span>Support</span><span>Contact Us</span><span>Terms &amp; Conditions</span><span>Privacy Policy</span>
  </nav>
</footer>
<footer class="legal-bar">
  <p>© 2016 Vortell Pty Ltd. All rights reserved.</p>
  <div class="social" aria-label="Social links"><span></span><span></span><span></span></div>
</footer>

</body>
</html>
```